A-Stand Directional Sign Design

Objective:
We need a professional graphic design for an A-Stand sign that will guide customers arriving in our parking lot to our office. The design should be visually clear, welcoming, and aligned with our brand identity.
REQUIREMENTS:
Two versions of the design:
- One with an arrow pointing left
- One with an arrow pointing right
(This allows us to place the A-Stand anywhere and flip the graphic as needed.)
DIMENSIONS:
- Viewable Area: 30" x 40"
BRAND ALIGNMENT:
- Colors, fonts, and overall style should match our website: www.skornabel.com
- Clean, modern, and professional look consistent with our aviation/tourism brand
CONTENT:
- Clear directional arrow (left or right depending on version)
- Text: “Office Entrance” or similar concise wording (designers may propose alternatives if they improve clarity)
READABILITY:
- Bold, high-contrast design for visibility from a distance
- Simple layout that avoids clutter
DELIVERABLES:
- Final artwork in print-ready format (PDF preferred)
- Two versions: Arrow Left and Arrow Right
DESIGN GOAL:
Ensure customers can easily find our office upon arrival, while reinforcing skorNABEL’s professional and welcoming brand image.
Target Market(s)
Tourism

```html
<!DOCTYPE html>
<html lang="en">
<head>
<meta charset="utf-8">
<title>skorNABEL A-Stand Directional Signs</title>
<link href="https://fonts.googleapis.com/css2?family=Montserrat:wght@600;700&display=swap" rel="stylesheet">
<style>
  :root {
    --backdrop: #c4c4c4;
    --sign-white: #ffffff;
    --brand-blue: #4067b1;
    --brand-deep: #2a78b8;
    --chevron-light: #a0bde6;
    --chevron-mid: #4d7bc0;
  }
  html, body {
    margin: 0;
    padding: 0;
    width: 1200px;
    height: 825px;
    overflow: hidden;
    background: var(--backdrop);
  }
  .canvas {
    position: relative;
    width: 1200px;
    height: 825px;
  }
  .sign {
    position: absolute;
    top: 78px;
    width: 503px;
    height: 670px;
    background: var(--sign-white);
    overflow: hidden;
    font-family: "Montserrat", sans-serif;
  }
  .sign--left { left: 70px; }
  .sign--right { left: 628px; }
  .sign__brand {
    position: absolute;
    top: 0;
    left: 0;
    width: 100%;
    height: 329px;
    display: flex;
    align-items: center;
    justify-content: center;
    gap: 14px;
  }
  .brand-mark {
    width: 34px;
    height: 34px;
    border-radius: 50%;
    background: var(--brand-deep);
  }
  .brand-name {
    font-size: 52px;
    font-weight: 700;
    color: var(--brand-deep);
    letter-spacing: 1px;
  }
  .sign__panel {
    position: absolute;
    top: 329px;
    left: 0;
    width: 100%;
    height: 341px;
    background: var(--brand-blue);
  }
  .sign__message {
    position: absolute;
    top: 40px;
    left: 0;
    width: 100%;
    margin: 0;
    text-align: center;
    color: var(--sign-white);
    font-weight: 700;
    font-size: 84px;
    line-height: 80px;
    letter-spacing: 1px;
  }
  .sign__arrows {
    position: absolute;
    top: 235px;
    left: 0;
    width: 100%;
    height: 72px;
  }
  .chevron {
    fill: none;
    stroke-width: 20;
    stroke-linecap: round;
    stroke-linejoin: round;
  }
  .chevron--white { stroke: var(--sign-white); }
  .chevron--light { stroke: var(--chevron-light); }
  .chevron--mid { stroke: var(--chevron-mid); }
</style>
</head>
<body>
<div class="canvas">

  <section class="sign sign--left" aria-label="Arrow left version">
    <div class="sign__brand">
      <span class="brand-mark"></span>
      <span class="brand-name">skorNABEL</span>
    </div>
    <div class="sign__panel">
      <h1 class="sign__message">Office<br>Entrance</h1>
      <svg class="sign__arrows" viewBox="0 0 503 72" aria-label="Arrows pointing left">
        <polyline class="chevron chevron--white" points="204,8 172,36 204,64"/>
        <polyline class="chevron chevron--light" points="267,8 235,36 267,64"/>
        <polyline class="chevron chevron--mid" points="336,8 304,36 336,64"/>
      </svg>
    </div>
  </section>

  <section class="sign sign--right" aria-label="Arrow right version">
    <div class="sign__brand">
      <span class="brand-mark"></span>
      <span class="brand-name">skorNABEL</span>
    </div>
    <div class="sign__panel">
      <h1 class="sign__message">Office<br>Entrance</h1>
      <svg class="sign__arrows" viewBox="0 0 503 72" aria-label="Arrows pointing right">
        <polyline class="chevron chevron--mid" points="167,8 199,36 167,64"/>
        <polyline class="chevron chevron--light" points="236,8 268,36 236,64"/>
        <polyline class="chevron chevron--white" points="299,8 331,36 299,64"/>
      </svg>
    </div>
  </section>

</div>
</body>
</html>
```